Business card design needed

I run a life coaching business.
I coach individuals, businesses & groups.
Our aim is create massive change for our clients.
I would like to see a card that is inspirational, something that provokes the thought of achieving your personal best.
Be your own inspiration is a phrase I am considering using.

Target Market(s)

People who are looking to create a massive change in their lives.

Industry/Entity Type

Life Coaching

Contact Information for Business Card

Harbor Light Coaching
Neil Pardoe
Head Coach
email neil@vorunel.com.au
Mob 0412 586 337

Logo styles of interest
Abstract Logo
Requirements
Must have
• I wouldlike to have a free introductory offer on the reverse side of the card.
It would read something like:
Is coaching for me/you?
Try a free 45 minute session.
Book now call or email for your appointment.

```html
<!DOCTYPE html>
<html lang="en">
<head>
<meta charset="utf-8">
<title>Harbor Light Coaching – Business Card</title>
<link rel="stylesheet" href="https://fonts.googleapis.com/css2?family=Questrial&display=swap">
<style>
  :root{
    --page:#f4f4f4;
    --card-light:#ececee;
    --card-dark:#2b3135;
    --card-dark-deep:#1f2427;
    --accent:#1ea3dc;
    --ink:#2a2f33;
    --text-light:#f2f2f2;
    --text-muted:#b9bcbe;
  }
  *{box-sizing:border-box;margin:0;padding:0}
  html,body{width:1200px;height:900px;overflow:hidden}
  body{
    background:var(--page);
    font-family:"Questrial","Century Gothic",sans-serif;
    display:flex;align-items:center;justify-content:center;gap:44px;
  }
  .card{
    position:relative;width:540px;height:330px;border-radius:22px;overflow:hidden;
    box-shadow:0 10px 24px rgba(0,0,0,.18);
  }
  /* Front */
  .card--front{background:var(--card-dark)}
  .front-top{
    position:absolute;left:0;top:0;width:100%;height:168px;background:var(--card-light);
    display:flex;align-items:flex-end;justify-content:center;padding-bottom:34px;
  }
  .front-stripe{position:absolute;left:0;top:168px;width:100%;height:12px;background:var(--accent)}
  .brand{display:flex;align-items:center;gap:12px}
  .brand-mark{width:20px;height:20px;border-radius:50%;background:var(--accent);flex:none}
  .brand-name{font-size:33px;letter-spacing:.5px;color:var(--ink);text-transform:uppercase;white-space:nowrap}
  .person{position:absolute;left:24px;top:194px}
  .person-name{font-size:18px;color:var(--accent)}
  .person-role{font-size:15px;color:var(--text-light);margin-top:2px}
  .contact{position:absolute;left:64px;top:250px;list-style:none}
  .contact li{display:flex;align-items:center;gap:6px;font-size:21px;color:var(--text-light);line-height:32px}
  .contact svg{width:20px;height:18px;flex:none}
  /* Back */
  .card--back{
    background:linear-gradient(160deg,var(--card-dark) 0%,var(--card-dark-deep) 100%);
    text-align:center;
  }
  .offer{position:absolute;left:0;right:0;top:84px}
  .offer p{line-height:31px}
  .offer-question{font-size:21px;color:var(--text-muted)}
  .offer-try{font-size:21px;color:var(--text-light)}
  .offer-try em{font-style:normal;color:var(--accent)}
  .offer-book{font-size:21px;color:var(--text-muted)}
  .back-brand{position:absolute;right:26px;bottom:60px}
  .back-brand .brand{gap:8px}
  .back-brand .brand-mark{width:13px;height:13px}
  .back-brand .brand-name{font-size:21px;color:var(--text-light)}
</style>
</head>
<body>
  <section class="card card--front" aria-label="Card front">
    <div class="front-top">
      <div class="brand"><span class="brand-mark"></span><span class="brand-name">Harbor Light Coaching</span></div>
    </div>
    <div class="front-stripe"></div>
    <div class="person">
      <p class="person-name">Neil Pardoe</p>
      <p class="person-role">Head Coach</p>
    </div>
    <ul class="contact">
      <li>
        <svg viewBox="0 0 20 18" aria-hidden="true"><path d="M2 6c0-3 4-4 8-4s8 1 8 4v2h-4V6H6v2H2z M5 9h10l2 7H3z" fill="#1ea3dc"/><circle cx="10" cy="12.5" r="2" fill="#2b3135"/></svg>
        0412 586 337
      </li>
      <li>
        <svg viewBox="0 0 20 18" aria-hidden="true"><rect x="1" y="3" width="18" height="12" fill="none" stroke="#1ea3dc" stroke-width="1.4"/><path d="M1 3l9 7 9-7" fill="none" stroke="#1ea3dc" stroke-width="1.4"/></svg>
        neil@vorunel.com.au
      </li>
    </ul>
  </section>

  <section class="card card--back" aria-label="Card back">
    <div class="offer">
      <p class="offer-question">Is coaching for me/you?</p>
      <p class="offer-try">Try a <em>free</em> 45 minute session</p>
      <p class="offer-book">Book now call or email for your appointment</p>
    </div>
    <div class="back-brand">
      <div class="brand"><span class="brand-mark"></span><span class="brand-name">Harbor Light Coaching</span></div>
    </div>
  </section>
</body>
</html>
```